Express envelope design for courier company

We're a courier company launching a new service for sending documents around Australia. We need a design for the express envelope that will be used to hold the documents during transit. The envelope will be printed in colour on cardboard. Please see brief attached.

Design cues:
• Vibrant
• Simplified
• Clean
• Aesthetically pleasing
• Artistic
• Nothing “institutional” or “Halvern Lines”
• Nothing cramped, no small text

It's fine to crop, recolour, or reinterpret the logo.

Industry/Entity Type

It Company

Font styles to use
Sans Serif

Requirements
Must have
• Dimensions:
• Back side: 350 x 230 mm
• Front side: 387.5 x 230 mm (including flap to close envelope)
• Back side barcode panel: 90 x 75 mm (blank area for adhesive barcode)
• Back side address panel: 150 x 90 mm (see PDF for contents and layout)
• Front side text:
• RM-ZO
• Express Envelope
• Send With Trust
• 1300 486 917
• rmzo-post.com.au
• Back side text:
• For documents
• Max. weight 500g, max width 20mm
• Send With Trust
• • Time-guaranteed and next-flight-out service for vital deliveries
• • Same-day and next-day local services
• • Overnight service to most Australian locations
• • Budget road service Australia-wide
• • Worldwide express courier
• Visit rmzo-post.com.au or phone 1300 486 917
• Flap text:
• Go to rmzo-post.com.au to book your pickup.
• Carried subject to RM-ZO Standard Conditions of Carriage; see our website.
Nice to have
• Our web colours:
• #fcd614
• #d06517
• #3b5274
• #f0f0d8
• #382a3a

```html
<!DOCTYPE html>
<html lang="en">
<head>
<meta charset="utf-8">
<title>RM-ZO Express Envelope</title>
<link rel="stylesheet" href="https://fonts.googleapis.com/css2?family=Arimo:ital,wght@0,400;0,700;1,700&display=swap">
<style>
  :root {
    --yellow: #fcd614;
    --orange: #d9692b;
    --navy: #3b5274;
    --cream: #f1f1da;
    --ink: #111111;
    --rule: #4a4a40;
    --white: #ffffff;
  }
  * { box-sizing: border-box; margin: 0; padding: 0; }
  html, body {
    width: 908px; height: 1200px; overflow: hidden;
    background: var(--white);
    font-family: "Arimo", Arial, sans-serif;
    color: var(--ink);
  }
  .artboard {
    position: relative;
    width: 850px; height: 1124px;
    transform: scale(1.0682);
    transform-origin: 0 0;
  }
  .panel { position: absolute; left: 0; width: 596px; height: 391px; background: var(--cream); }
  .panel--front { top: 68px; }
  .panel--back { top: 565px; }

  .brand-name {
    position: absolute; left: 236px; top: 56px;
    font-size: 36px; font-weight: 700; line-height: 1;
    color: var(--ink);
  }
  .product-name {
    position: absolute; left: 337px; top: 125px;
    font-size: 14px; font-weight: 700;
  }

  .tagline-rule { position: absolute; height: 4px; background: var(--navy); }
  .tagline {
    position: absolute;
    font-size: 14.5px; font-weight: 700; font-style: italic; line-height: 1;
  }

  .contact-bar {
    position: absolute; left: 0; bottom: 0; width: 596px; height: 19px;
    background: var(--navy); border-top: 2px solid #26344c;
    color: var(--white); font-size: 9.5px; font-weight: 700;
  }
  .contact-item { position: absolute; top: 3px; display: flex; align-items: center; gap: 3px; line-height: 1; }
  .contact-item svg { width: 12px; height: 12px; }
  .contact-note { position: absolute; right: 17px; top: 3px; }

  .flap { position: absolute; left: 596px; top: 68px; width: 64px; height: 391px; }
  .flap-text {
    position: absolute; left: 624px; top: 263px;
    transform: translate(-50%, -50%) rotate(-90deg);
    white-space: nowrap; color: var(--white);
    font-size: 9.5px; font-weight: 700; line-height: 16px; text-align: center;
  }

  .service-list {
    position: absolute; left: 180px; top: 37px; list-style: none;
    font-size: 10.5px;
  }
  .service-list li { position: relative; padding-left: 13px; height: 21.7px; }
  .service-list li::before { content: "•"; position: absolute; left: 0; }

  .barcode-area {
    position: absolute; left: 17px; top: 241px; width: 154px; height: 128px;
    border: 1px solid var(--rule);
  }
  .address-panel {
    position: absolute; left: 187px; top: 216px; width: 256px; height: 154px;
    border: 1px solid var(--rule);
    display: grid; grid-template-rows: 42px 98px 1fr; grid-template-columns: 111px 1fr;
    font-size: 9px;
  }
  .address-field { padding: 4px 5px; border-bottom: 1px solid var(--rule); grid-column: 1 / 3; }
  .address-field--short { grid-column: auto; border-bottom: none; padding: 1px 5px; }
  .address-field--short + .address-field--short { border-left: 1px solid var(--rule); }
</style>
</head>
<body>
<div class="artboard">

  <section class="panel panel--front">
    <div class="brand-name">RM-ZO</div>
    <div class="product-name">Express Envelope</div>

    <div class="tagline-rule" style="left:0; top:193px; width:331px"></div>
    <div class="tagline" style="left:337px; top:187px">Ship With Trust</div>
    <div class="tagline-rule" style="left:451px; top:193px; width:145px"></div>

    <div class="contact-bar">
      <span class="contact-item" style="left:118px">
        <svg viewBox="0 0 24 24"><path fill="#fff" d="M6.6 10.8a15.1 15.1 0 0 0 6.6 6.6l2.2-2.2a1 1 0 0 1 1-.25 11.4 11.4 0 0 0 3.6.57 1 1 0 0 1 1 1V20a1 1 0 0 1-1 1A17 17 0 0 1 3 4a1 1 0 0 1 1-1h3.5a1 1 0 0 1 1 1c0 1.25.2 2.45.57 3.570a1 1 0 0 1-.25 1z"/></svg>
        1300 486 917
      </span>
      <span class="contact-item" style="left:405px">
        <svg viewBox="0 0 24 24"><circle cx="12" cy="12" r="10" fill="#fff"/><path d="M2 12h20M12 2c3 3 3 17 0 20M12 2c-3 3-3 17 0 20" stroke="#3b5274" stroke-width="1.6" fill="none"/></svg>
        rmzo-post.com.au
      </span>
    </div>
  </section>

  <svg class="flap" viewBox="0 0 64 391"><polygon points="0,0 64,18 64,373 0,391" fill="var(--orange)"/></svg>
  <p class="flap-text">Go to rmzo-post.com.au to book your pickup.<br>Carried subject to RM-ZO Standard Conditions of Carriage; see our website.</p>

  <section class="panel panel--back">
    <div class="tagline-rule" style="left:0; top:22px; width:175px"></div>
    <div class="tagline" style="left:181px; top:16px">Ship With Trust</div>
    <div class="tagline-rule" style="left:293px; top:22px; width:303px"></div>

    <ul class="service-list">
      <li>Time-guaranteed and next-flight-out service for vital deliveries</li>
      <li>Same-day and next-day local services</li>
      <li>Overnight service to most Australian locations</li>
      <li>Budget road service Australia-wide</li>
      <li>Worldwide express courier</li>
    </ul>

    <div class="barcode-area" aria-label="Space for adhesive barcode"></div>

    <div class="address-panel">
      <div class="address-field">Sender’s Name</div>
      <div class="address-field">Receiver</div>
      <div class="address-field address-field--short">State</div>
      <div class="address-field address-field--short">Postcode</div>
    </div>

    <div class="contact-bar">
      <span class="contact-item" style="left:17px">
        <svg viewBox="0 0 24 24"><path fill="#fff" d="M6.6 10.8a15.1 15.1 0 0 0 6.6 6.6l2.2-2.2a1 1 0 0 1 1-.25 11.4 11.4 0 0 0 3.6.57 1 1 0 0 1 1 1V20a1 1 0 0 1-1 1A17 17 0 0 1 3 4a1 1 0 0 1 1-1h3.5a1 1 0 0 1 1 1c0 1.25.2 2.45.57 3.57a1 1 0 0 1-.25 1z"/></svg>
        1300 486 917
      </span>
      <span class="contact-item" style="left:134px">
        <svg viewBox="0 0 24 24"><circle cx="12" cy="12" r="10" fill="#fff"/><path d="M2 12h20M12 2c3 3 3 17 0 20M12 2c-3 3-3 17 0 20" stroke="#3b5274" stroke-width="1.6" fill="none"/></svg>
        rmzo-post.com.au
      </span>
      <span class="contact-note">For documents: Max. weight 500g, max width 20mm</span>
    </div>
  </section>

</div>
</body>
</html>
```